Pinecrest Renovations - Get the creative juices going!!

Pinecrest does not do the actual renovation work. The company provides high end project management of renovation (primarily residential - with an eye toward commercial) The renovation work could look very different between projects. This company manages the work of contractors, architects and interior designers (either subcontracted directly by Pinecrest or hired by the client and entrusted to Pinecrest to manage). Clients are high end in the economic scale and the card needs to have a high end feel to it.

The owner is female, but the audience will be heavily slanted male. It should not be a "feminine" or "masculine" looking card. If anything, slant more on the masculine side. Clean, simple, yet creative and artistically appealing. The card design should complement and in no way compete with the logo.

When people think of our company: trust, integrity, dynamic, limitless possibilities, transition, energy, creative. We plan to expand in the future to be international.

There will also be a contest running for stationary. Please check that section, as well.

***Black is 80-90 percent black. Not stark black

Tight timeline. Needs cards printed quickly!

Residential

```html
<!DOCTYPE html>
<html lang="en">
<head>
<meta charset="utf-8">
<title>Pinecrest Renovations – Business Card</title>
<link rel="stylesheet" href="https://fonts.googleapis.com/css2?family=Montserrat:wght@400;600;700&display=swap">
<style>
  :root {
    --charcoal: #3b3b3e;
    --teal: #1fa99a;
    --paper: #ffffff;
    --stage: #e6e6e6;
    --muted: #d8d8d8;
    --card-w: 520px;
    --card-h: 297px;
  }
  * { box-sizing: border-box; margin: 0; padding: 0; }
  html, body {
    width: 1200px; height: 597px; overflow: hidden;
    background: var(--stage);
    font-family: "Montserrat", sans-serif;
  }
  .stage {
    position: relative; width: 1200px; height: 597px;
    display: flex; align-items: center; justify-content: center; gap: 40px;
  }
  .card {
    position: relative; width: var(--card-w); height: var(--card-h);
    overflow: hidden; background: var(--charcoal);
    box-shadow: 0 6px 18px rgba(0,0,0,.18);
  }
  .card__stripe {
    position: absolute; left: 0; right: 0; bottom: 0; height: 18px;
    background: var(--teal);
  }

  /* Front */
  .front__header {
    position: absolute; left: 0; top: 0; right: 0; height: 118px;
    background: var(--paper);
  }
  .front__notch {
    position: absolute; top: 117px; right: 34px; width: 18px; height: 10px;
  }
  .brand-name {
    position: absolute; right: 34px; top: 76px;
    font-weight: 700; font-size: 17px; letter-spacing: 1px;
    color: var(--charcoal); text-transform: uppercase; white-space: nowrap;
  }
  .contact-list {
    position: absolute; right: 20px; top: 140px;
    list-style: none; display: flex; flex-direction: column; gap: 8px;
  }
  .contact-list__item {
    display: flex; align-items: flex-start; justify-content: flex-end; gap: 10px;
    color: var(--paper); font-size: 10.5px; line-height: 1.25; text-align: right;
    letter-spacing: .3px;
  }
  .contact-list__text { padding-top: 4px; }
  .icon-box {
    flex: none; width: 20px; height: 20px; background: var(--teal);
    display: flex; align-items: center; justify-content: center;
  }
  .icon-box svg { width: 12px; height: 12px; }
  .person {
    position: absolute; left: 20px; top: 212px;
    display: flex; gap: 12px; align-items: flex-start;
  }
  .person__name { color: var(--paper); font-weight: 700; font-size: 15px; line-height: 1.1; }
  .person__role { color: var(--muted); font-weight: 400; font-size: 13px; margin-top: 2px; }

  /* Back */
  .back { display: flex; align-items: center; justify-content: center; }
  .back__brand-name {
    margin-bottom: 18px;
    color: var(--paper); font-weight: 600; font-size: 25px;
    letter-spacing: 3px; text-transform: uppercase; white-space: nowrap;
  }
</style>
</head>
<body>
<main class="stage">

  <section class="card front" aria-label="Card front">
    <div class="front__header"></div>
    <svg class="front__notch" viewBox="0 0 18 10" aria-hidden="true"><polygon points="0,0 18,0 9,10" fill="#ffffff"/></svg>
    <p class="brand-name">Pinecrest Renovations</p>

    <ul class="contact-list">
      <li class="contact-list__item">
        <span class="contact-list__text">555 204 7130</span>
        <span class="icon-box"><svg viewBox="0 0 12 12" aria-hidden="true"><rect x="3" y="1" width="6" height="10" rx="1" fill="none" stroke="#fff" stroke-width="1.2"/><circle cx="6" cy="9.3" r=".6" fill="#fff"/></svg></span>
      </li>
      <li class="contact-list__item">
        <span class="contact-list__text">www.pinecrestreno.com</span>
        <span class="icon-box"><svg viewBox="0 0 12 12" aria-hidden="true"><circle cx="6" cy="6" r="4.6" fill="none" stroke="#fff" stroke-width="1.2"/><path d="M1.4 6h9.2M6 1.4c-2 2.5-2 6.7 0 9.2M6 1.4c2 2.5 2 6.7 0 9.2" fill="none" stroke="#fff" stroke-width=".9"/></svg></span>
      </li>
      <li class="contact-list__item">
        <span class="contact-list__text">hello@pinecrestreno.com</span>
        <span class="icon-box"><svg viewBox="0 0 12 12" aria-hidden="true"><rect x="1" y="2.5" width="10" height="7" fill="none" stroke="#fff" stroke-width="1.1"/><path d="M1 2.5l5 4 5-4" fill="none" stroke="#fff" stroke-width="1.1"/></svg></span>
      </li>
      <li class="contact-list__item">
        <span class="contact-list__text">128 N. Harbor Lane,<br>Fairview CA 90510</span>
        <span class="icon-box"><svg viewBox="0 0 12 12" aria-hidden="true"><path d="M6 11.2S2.2 7 2.2 4.6a3.8 3.8 0 0 1 7.6 0C9.8 7 6 11.2 6 11.2z" fill="#fff"/><circle cx="6" cy="4.6" r="1.4" fill="#1fa99a"/></svg></span>
      </li>
    </ul>

    <div class="person">
      <span class="icon-box"><svg viewBox="0 0 12 12" aria-hidden="true"><circle cx="6" cy="4" r="2.3" fill="#fff"/><path d="M1.8 11c0-2.6 1.9-4 4.2-4s4.2 1.4 4.2 4z" fill="#fff"/></svg></span>
      <div>
        <p class="person__name">Your Name</p>
        <p class="person__role">Designation</p>
      </div>
    </div>

    <div class="card__stripe"></div>
  </section>

  <section class="card back" aria-label="Card back">
    <p class="back__brand-name">Pinecrest Renovations</p>
    <div class="card__stripe"></div>
  </section>

</main>
</body>
</html>
```